Adult Toys 1hr Delivery Billboard

We need a digital billboard.
We are
Zipwo.ca
Adult toys 1hr delivery
WE DELIVER FROM from 11am to 3am 7 days a week
we only deliver in Toronto Canada
we use zipwo.ca for marketing and branding but the company name is (Bright Lark Parcel Runners.com )
Fast safe and discreet
keep a private purchase private
We're ready when you're ready
WE deliver to you home, hotel or favorite coffee shop
please visit our website for any other information you may need

if you want to watch our videos for any inspiration here is our youtube channel

https://www.vidplexo.example/channel/UQxRbNLT4pHzGkwY7vJmYs2e

it is a digital bill board with only 6 sec impressions
cars will be traveling at 100km when passing the billboard so message must be
to the point with the least amount of words
provocative or fun enough to get peoples attention but being "adult toys" sill must be approved by billboard supplier and city so we may choose a winner based on city approval as well.

our main message is Adult toys 1hr delivery

Ive also sent two billboard photos of one of my competitors that were very successful for them. again please note those are from my main competitor. We really need to top their campaign but if you notice theirs was very short and sweet. THEY DON'T OFFER 1HR DELIVERY. we are the only ones in Canada and are the first in the world.

Target Market(s)

men and women 25 to 45

Industry/Entity Type

Adult

Requirements
Must have
• This must be main message "Adult toys 1hr delivery"
Nice to have
• message must be short
we deliver from 11am to 3am
can we put faster than quorvel ?
bright fun attention getting
Should not have
• should not have the word

sex

```html
<!DOCTYPE html>
<html lang="en">
<head>
<meta charset="utf-8">
<title>Zipwo.ca – 1HR Adult Toys Delivery Billboard</title>
<link rel="stylesheet" href="https://fonts.googleapis.com/css2?family=Lexend:wght@700&family=Questrial&display=swap">
<style>
  :root {
    --board-bg: #e8e8ee;
    --gold: #f2c21e;
    --gold-deep: #e3a321;
    --band-gold: #e9b52c;
    --band-red: #e2412f;
    --frame-gold: #dfa42a;
    --frame-red: #e0403a;
    --ink: #2a2440;
    --white: #ffffff;
  }
  html, body {
    margin: 0;
    padding: 0;
    width: 1200px;
    height: 801px;
    overflow: hidden;
    background: var(--board-bg);
  }
  .billboard {
    position: relative;
    width: 1200px;
    height: 801px;
    background: var(--board-bg);
    overflow: hidden;
    font-family: "Questrial", sans-serif;
  }
  .brush-backdrop {
    position: absolute;
    left: 160px;
    top: 200px;
    width: 860px;
    height: 520px;
  }
  .frame {
    position: absolute;
    left: 280px;
    top: 140px;
    width: 690px;
    height: 500px;
    border: 5px solid;
    border-bottom: none;
    border-image: linear-gradient(90deg, var(--frame-gold), var(--frame-red)) 1;
    box-sizing: border-box;
  }
  .brand {
    position: absolute;
    left: 430px;
    top: 248px;
    display: flex;
    align-items: center;
    gap: 14px;
  }
  .brand-dot {
    width: 42px;
    height: 42px;
    border-radius: 50%;
    background: var(--white);
  }
  .brand-name {
    font-size: 48px;
    color: var(--white);
    line-height: 1;
  }
  .brand-tagline {
    position: absolute;
    left: 488px;
    top: 306px;
    font-size: 12px;
    letter-spacing: 1px;
    color: var(--white);
    text-transform: uppercase;
  }
  .headline {
    margin: 0;
    font-size: inherit;
    font-weight: inherit;
  }
  .headline-hour {
    position: absolute;
    left: 326px;
    top: 322px;
    font-family: "Lexend", sans-serif;
    font-weight: 700;
    font-size: 200px;
    line-height: 1;
    letter-spacing: -5px;
    background: linear-gradient(180deg, var(--gold), var(--gold-deep));
    -webkit-background-clip: text;
    background-clip: text;
    color: transparent;
  }
  .headline-word {
    position: absolute;
    color: var(--gold);
    line-height: 1;
  }
  .headline-adult { left: 736px; top: 380px; font-size: 62px; letter-spacing: 2px; }
  .headline-toys  { left: 740px; top: 450px; font-size: 62px; letter-spacing: 12px; }
  .headline-delivery { left: 330px; top: 528px; font-size: 78px; letter-spacing: 20px; }
  .service-band {
    position: absolute;
    left: 0;
    top: 640px;
    width: 1200px;
    height: 80px;
    box-sizing: border-box;
    padding-left: 330px;
    display: flex;
    align-items: center;
    background: linear-gradient(90deg, var(--band-gold) 0%, var(--band-gold) 45%, var(--band-red) 100%);
  }
  .service-area {
    margin: 0;
    font-size: 36px;
    color: var(--ink);
    line-height: 1;
  }
  .service-area strong {
    font-weight: 400;
    letter-spacing: 1px;
  }
</style>
</head>
<body>
  <main class="billboard">
    <svg class="brush-backdrop" viewBox="0 0 860 520" role="img" aria-label="Red painted brush-stroke backdrop">
      <defs>
        <linearGradient id="brushFill" x1="0" y1="0" x2="1" y2="1">
          <stop offset="0" stop-color="#d02d3e"/>
          <stop offset="1" stop-color="#8c1a35"/>
        </linearGradient>
      </defs>
      <path d="M150 40 Q430 0 690 50 Q820 120 840 300 Q850 440 770 505 Q470 530 180 490 Q30 440 20 280 Q40 90 150 40 Z" fill="url(#brushFill)"/>
    </svg>

    <div class="frame"></div>

    <div class="brand">
      <span class="brand-dot"></span>
      <span class="brand-name">Zipwo.ca</span>
    </div>
    <div class="brand-tagline">Bright Lark Parcel Runners</div>

    <h1 class="headline">
      <span class="headline-hour">1HR</span>
      <span class="headline-word headline-adult">ADULT</span>
      <span class="headline-word headline-toys">TOYS</span>
      <span class="headline-word headline-delivery">DELIVERY</span>
    </h1>

    <div class="service-band">
      <p class="service-area">We Only Deliver In <strong>TORONTO CANADA</strong></p>
    </div>
  </main>
</body>
</html>
```